Professional Photography Business cards

I need business cards that include my logo which I have uploaded. I run a photography business. I am open to ideas but I would like one side to have my logo and the other side to have my contact info. I don't have a website made but I do own a website domain. I have uploaded 2 different logo color schemes. My business colors are Blue, black , and white.

Business Name
Business Phone Number
Business Email
Business Website address
Instagram

Industry/Entity Type

Professional Photography

Contact Information for Business Card

Phone Number: 555-314-8027 email: info@tkellan-studios.example Instagram: @t.kellanstudios website doman- www.tkellan-studios.example

Requirements
Must have
• I like the idea of a business card with a full black background front and back of card. My colors must include royal blue, black, and white

```html
<!DOCTYPE html>
<html lang="en">
<head>
<meta charset="utf-8">
<title>T. Kellan Studios – Business Card</title>
<link href="https://fonts.googleapis.com/css2?family=Arimo:wght@400;700&display=swap" rel="stylesheet">
<style>
  :root {
    --backdrop: #3b3b3c;
    --card: #1c1c1d;
    --royal-blue: #2f35a3;
    --white: #ffffff;
    --emboss: #2a2a2b;
    --emboss-edge: #6d6d6f;
  }
  * { margin: 0; padding: 0; box-sizing: border-box; }
  html, body {
    width: 1200px;
    height: 1059px;
    overflow: hidden;
    background: var(--backdrop);
    font-family: "Arimo", Arial, sans-serif;
  }
  .card {
    position: absolute;
    left: 255px;
    width: 690px;
    height: 392px;
    background: var(--card);
    border-radius: 22px;
    box-shadow: 0 10px 24px rgba(0,0,0,0.55);
  }
  .card--front { top: 100px; }
  .card--back { top: 537px; }

  /* Front: embossed wordmark */
  .front-mark {
    position: absolute;
    left: 0; right: 0;
    top: 150px;
    display: flex;
    align-items: center;
    justify-content: center;
    gap: 18px;
  }
  .front-mark__name {
    font-size: 40px;
    font-weight: 400;
    color: var(--emboss);
    letter-spacing: 1px;
  }
  .front-mark__circle {
    width: 70px;
    height: 70px;
    border-radius: 50%;
    border: 5px solid var(--emboss-edge);
  }

  /* Back: contact side */
  .back-mark {
    position: absolute;
    left: 29px;
    top: 52px;
    display: flex;
    align-items: center;
    gap: 14px;
  }
  .back-mark__name {
    font-size: 30px;
    font-weight: 400;
    color: var(--royal-blue);
  }
  .back-mark__circle {
    width: 52px;
    height: 52px;
    border-radius: 50%;
    border: 4px solid var(--white);
  }
  .person {
    position: absolute;
    right: 27px;
    top: 174px;
    text-align: right;
  }
  .person__name {
    font-size: 27px;
    font-weight: 700;
    color: var(--royal-blue);
    line-height: 1;
  }
  .person__title {
    font-size: 16px;
    color: var(--white);
    margin-top: 4px;
  }
  .divider {
    position: absolute;
    left: 29px;
    right: 27px;
    top: 234px;
    height: 1px;
    background: var(--royal-blue);
  }
  .contacts {
    position: absolute;
    left: 29px;
    top: 280px;
    list-style: none;
  }
  .contacts__item {
    display: flex;
    align-items: center;
    gap: 8px;
    height: 21.3px;
    font-size: 16.5px;
    color: var(--white);
  }
  .contacts__icon {
    width: 12px;
    height: 12px;
    flex: none;
  }
</style>
</head>
<body>
  <section class="card card--front">
    <div class="front-mark">
      <span class="front-mark__name">T. Kellan Studios</span>
      <span class="front-mark__circle"></span>
    </div>
  </section>

  <section class="card card--back">
    <div class="back-mark">
      <span class="back-mark__name">T. Kellan Studios</span>
      <span class="back-mark__circle"></span>
    </div>

    <div class="person">
      <div class="person__name">Dana Morel</div>
      <div class="person__title">Managing Director</div>
    </div>

    <div class="divider"></div>

    <ul class="contacts">
      <li class="contacts__item">
        <svg class="contacts__icon" viewBox="0 0 24 24"><path fill="#2f35a3" d="M6.6 10.8a15.1 15.1 0 0 0 6.6 6.6l2.2-2.2a1 1 0 0 1 1-.25 11.4 11.4 0 0 0 3.6.57 1 1 0 0 1 1 1V20a1 1 0 0 1-1 1A17 17 0 0 1 3 4a1 1 0 0 1 1-1h3.5a1 1 0 0 1 1 1c0 1.25.2 2.45.57 3.57a1 1 0 0 1-.25 1z"/></svg>
        <span>555-314-8027</span>
      </li>
      <li class="contacts__item">
        <svg class="contacts__icon" viewBox="0 0 24 24"><rect x="1" y="5" width="22" height="14" fill="#2f35a3"/><path d="M1 5l11 8 11-8M1 19l8-7M23 19l-8-7" stroke="#1c1c1d" stroke-width="1.6" fill="none"/></svg>
        <span>info@tkellan-studios.example</span>
      </li>
      <li class="contacts__item">
        <svg class="contacts__icon" viewBox="0 0 24 24"><circle cx="12" cy="12" r="10" fill="#2f35a3"/><path d="M2 12h20M12 2c3 3 3 17 0 20M12 2c-3 3-3 17 0 20" stroke="#1c1c1d" stroke-width="1.4" fill="none"/></svg>
        <span>www.tkellan-studios.example</span>
      </li>
      <li class="contacts__item">
        <svg class="contacts__icon" viewBox="0 0 24 24"><rect x="2" y="2" width="20" height="20" rx="3" fill="#2f35a3"/></svg>
        <span>@t.kellanstudios</span>
      </li>
    </ul>
  </section>
</body>
</html>
```